Flyer-Design für Kurierdienst
Der gedruckte Flyer ist heute bei uns angekommen. Wir sind mit der Arbeit sehr zufrieden.
Zielgruppe
Wir sind ein Kurierdienst in Frankfurt am Main. Der Flyer soll auf unsere drei Kerndienstleistungen aufmerksam machen. Diese sind Direktfahrten innerhalb von Frankfurt, Deutschland und Europa, der nationale Versand über Nacht sowie der internationale Expressversand.
Unsere Zielgruppe sind ausschließlich Firmenkunden in Frankfurt. Vor allem möchten wir mit dem Flyer anspruchsvolle Kunden wie z.B. Anwaltskanzleien und Finanzdienstleister erreichen. Wir bieten einen Rundum-Service, geschulte Fahrer und feste Ansprechpartner (kein Callcenter).
Eine genauere Beschreibung unserer Dienstleistungen hängt an bzw. sind auf unserer Internetseite unter www.lindenhofmobil.com zu finden.
Aufgabenstellung
Wir haben uns einen zwei- oder vierseitigen DIN-Lang Flyer vorgestellt. Farblich sollte sich der Flyer am blau aus unserem Logo orientieren. Das angehangene "Die Lerche" Logo darf nur in Verbindung mit dem nationalen Versand über Nacht aufgeführt werden. Unsere Telefonnummer solle auf der Frontseite deutlich hervorgehoben sein.

```html
<!DOCTYPE html>
<html lang="de">
<head>
<meta charset="utf-8">
<title>Lindenhof Mobil – Flyer</title>
<link href="https://fonts.googleapis.com/css2?family=Inter:wght@300;400;500;600&display=swap" rel="stylesheet">
<style>
  :root {
    --brand-blue: #1f5f94;
    --band-blue: #6ab3e0;
    --white: #ffffff;
    --sky-top: #8e9fd2;
    --sky-mid: #b9cbe6;
    --sky-haze: #dfe6ee;
    --city-steel: #8d9db8;
    --city-warm: #cdb48f;
    --city-shade: #8f7a63;
  }
  * { margin: 0; padding: 0; box-sizing: border-box; }
  html, body {
    width: 1189px; height: 1200px; overflow: hidden;
    background: var(--white);
    font-family: "Inter", Helvetica, Arial, sans-serif;
  }
  .flyer { position: relative; width: 1189px; height: 1200px; overflow: hidden; background: var(--white); }

  .brand {
    position: absolute; left: 680px; top: 54px;
    display: flex; align-items: center; gap: 14px;
  }
  .brand-dot { width: 26px; height: 26px; border-radius: 50%; background: var(--brand-blue); }
  .brand-name {
    font-weight: 600; font-size: 39px; letter-spacing: 0.5px;
    color: var(--brand-blue); text-transform: uppercase;
  }

  .city-photo {
    position: absolute; left: 0; top: 190px; width: 1189px; height: 1010px;
    background:
      radial-gradient(ellipse 420px 260px at 900px 560px, rgba(255,244,220,0.75), rgba(255,244,220,0) 70%),
      radial-gradient(ellipse 520px 220px at 260px 300px, rgba(255,255,255,0.45), rgba(255,255,255,0) 70%),
      linear-gradient(180deg,
        var(--sky-top) 0%,
        var(--sky-mid) 28%,
        var(--sky-haze) 46%,
        var(--city-steel) 58%,
        #a9a9ab 68%,
        var(--city-warm) 80%,
        var(--city-shade) 100%);
  }

  .claim-box {
    position: absolute; left: 676px; top: 250px; width: 356px; height: 217px;
  }
  .claim-box svg { position: absolute; inset: 0; filter: drop-shadow(2px 3px 4px rgba(0,0,0,0.25)); }
  .claim-list {
    position: absolute; left: 34px; top: 22px; list-style: none;
    color: var(--white); font-weight: 500; font-size: 45px; line-height: 56px;
  }

  .info-band { position: absolute; left: 0; top: 0; width: 1189px; height: 1200px; pointer-events: none; }

  .imprint {
    position: absolute; left: 45px; top: 1058px; font-style: normal;
    color: var(--white); font-weight: 300; font-size: 18px; line-height: 25px;
  }
  .imprint-title { font-weight: 600; }

  .contact {
    position: absolute; left: 680px; top: 1040px; width: 422px;
    text-align: center; color: var(--white);
    font-weight: 300; font-size: 26px; line-height: 36px;
  }
</style>
</head>
<body>
<main class="flyer">
  <header class="brand">
    <span class="brand-dot"></span>
    <span class="brand-name">Lindenhof Mobil</span>
  </header>

  <div class="city-photo" role="img" aria-label="Foto der Frankfurter Skyline mit Hochhäusern, Kirchturm und Altstadtdächern unter blauem Himmel"></div>

  <section class="claim-box">
    <svg width="356" height="217" viewBox="0 0 356 217">
      <polygon points="0,0 356,0 307,217 0,217" fill="var(--brand-blue)"/>
    </svg>
    <ul class="claim-list">
      <li>Schnell</li>
      <li>Flexibel</li>
      <li>Zuverlässig</li>
    </ul>
  </section>

  <svg class="info-band" width="1189" height="1200" viewBox="0 0 1189 1200">
    <polygon points="0,1043 1189,966 1189,1200 0,1200" fill="var(--band-blue)"/>
  </svg>

  <address class="imprint">
    <div class="imprint-title">Impressum</div>
    <div>Lindenhof Mobil</div>
    <div>Birkenweg 12</div>
    <div>60311 Frankfurt am Main</div>
  </address>

  <p class="contact">
    Sie erreichen uns unter<br>
    Tel.: 069 - 5550123-0 oder per<br>
    mail an info@lindenhofmobil.com
  </p>
</main>
</body>
</html>
```